Business Card, Stationery, Folder and Notepad Design
I need double sided standard sized Business Card [3.5" x 2"]
up to designer
Professional
Wes Harlan
27400 W. Pelham Rd.
Pine Hollow
IL
415-932-7104 ext 582
wessy@quillmarkdeeds.example
I don't want to see just the business card designs. Please submit a design for all four things mentioned otherwise it will be eliminated.
Order Now at www.quillmarkdeeds.example

```html
<!DOCTYPE html>
<html lang="en">
<head>
<meta charset="utf-8">
<title>Quillmark Deeds – Stationery Set</title>
<link href="https://fonts.googleapis.com/css2?family=Cinzel:wght@700&family=Open+Sans:wght@400;600&display=swap" rel="stylesheet">
<style>
  :root{
    --ink:#111111;
    --paper:#ffffff;
    --gold:#d9902a;
    --gold-light:#f3c46a;
    --grey:#8a8a8a;
    --stage:#ececec;
  }
  *{box-sizing:border-box;margin:0;padding:0}
  html,body{width:1200px;height:367px;overflow:hidden;background:var(--stage)}
  body{position:relative;font-family:"Open Sans",sans-serif;color:var(--ink)}
  .piece{position:absolute;background:var(--paper);box-shadow:0 2px 5px rgba(0,0,0,.25);overflow:hidden}
  .brand{position:absolute;display:flex;align-items:center;gap:4px}
  .brand-mark{width:8px;height:8px;background:var(--gold);flex:none}
  .brand-name{font-family:"Cinzel",serif;font-weight:700;font-size:7.5px;color:var(--gold);white-space:nowrap;line-height:1}
  .tagline{font-size:6px;color:var(--grey);white-space:nowrap}
  .swirl-art{position:absolute;background:radial-gradient(ellipse at 50% 50%,rgba(217,144,42,.2),rgba(255,255,255,0) 68%)}
  .band{position:absolute;left:0;bottom:0;width:100%;display:block}
  .footer-text{position:absolute;right:6px;bottom:4px;font-size:3.4px;color:#cfcfcf;text-align:right;line-height:1.3;white-space:nowrap}

  /* presentation folder */
  .folder-outer{left:12px;top:19px;width:216px;height:317px;background:var(--ink)}
  .folder-outer .swirl-art{left:8px;top:6px;width:200px;height:230px;background:radial-gradient(ellipse at 40% 45%,#b9b1a4,#4a4640 55%,var(--ink) 75%)}
  .folder-outer .brand{left:18px;top:262px;flex-direction:column;align-items:flex-start;gap:5px}
  .folder-outer .brand-name{font-size:15px;color:var(--paper)}
  .folder-inner{left:228px;top:19px;width:204px;height:317px}
  .folder-inner .swirl-art{left:12px;top:30px;width:180px;height:200px}
  .folder-pocket{position:absolute;left:0;bottom:0;width:100%;height:110px}

  /* fax and letterhead */
  .sheet{top:19px;width:190px;height:281px}
  .sheet .brand{left:8px;top:8px}
  .sheet .swirl-art{left:15px;top:70px;width:160px;height:180px}
  .fax{left:439px}
  .letterhead{left:641px}
  .fax-title{position:absolute;right:12px;top:24px;font-size:6px;font-weight:600}
  .fax-table{position:absolute;left:12px;top:34px;width:166px;border-collapse:collapse;font-size:4px}
  .fax-table td{border:.5px solid #999;height:9px;padding:0 2px}

  /* large envelope */
  .envelope-c{left:840px;top:19px;width:216px;height:156px}
  .envelope-c .brand{left:8px;top:8px}
  .envelope-c .swirl-art{left:50px;top:18px;width:120px;height:110px}

  /* notepad */
  .notepad{left:1085px;top:19px;width:96px;height:197px}
  .notepad .brand{left:6px;top:8px}
  .notepad .brand-name{font-size:6.5px}
  .notepad .swirl-art{left:8px;top:40px;width:80px;height:120px}

  /* DL envelopes */
  .dl-envelope{left:840px;width:216px;height:60px}
  .dl-front{top:228px}
  .dl-front .brand{left:8px;top:8px}
  .dl-back{top:293px}
  .dl-back .flap{position:absolute;left:0;top:0;width:100%;height:30px;background:linear-gradient(90deg,#7a4410,var(--gold),#7a4410)}
  .dl-back .seal{position:absolute;left:100px;top:22px;width:16px;height:16px;border-radius:50%;background:var(--ink)}

  /* business cards */
  .card{top:295px;width:72px;height:38px}
  .card .brand{left:4px;top:4px;gap:3px}
  .card .brand-mark{width:6px;height:6px}
  .card .brand-name{font-size:5px}
  .card-dark{background:var(--ink)}
  .card-dark .brand{left:50%;top:50%;transform:translate(-50%,-50%)}
  .card-name{position:absolute;left:4px;top:15px;font-size:4px;font-weight:600;white-space:nowrap}
  .card-info{position:absolute;left:4px;top:21px;font-size:2.8px;color:#444;line-height:1.35;white-space:nowrap}
  .card-grey{background:linear-gradient(135deg,#bbb,#555)}
  .card-gold{background:linear-gradient(135deg,var(--gold-light),var(--gold))}
</style>
</head>
<body>

<section class="piece folder-outer">
  <div class="swirl-art" role="img" aria-label="Large abstract ribbon swirl in silver and gold tones"></div>
  <div class="brand">
    <span class="brand-name">Quillmark Deeds</span>
    <span class="tagline">Title &amp; Escrow Services</span>
  </div>
</section>
<section class="piece folder-inner">
  <div class="swirl-art" role="img" aria-label="Faint gold ribbon swirl watermark"></div>
  <div class="folder-pocket">
    <svg class="band" viewBox="0 0 204 110" width="204" height="110" preserveAspectRatio="none">
      <path d="M0 26 Q102 0 204 14 L204 110 L0 110Z" fill="var(--ink)"/>
      <path d="M0 30 Q102 4 204 18" stroke="var(--gold)" stroke-width="2" fill="none"/>
    </svg>
    <div class="footer-text">27400 W. Pelham Rd. Pine Hollow, IL<br>www.quillmarkdeeds.example</div>
  </div>
</section>

<section class="piece sheet fax">
  <div class="brand"><span class="brand-mark"></span><span class="brand-name">Quillmark Deeds</span></div>
  <div class="fax-title">FAX</div>
  <table class="fax-table">
    <tr><td>To:</td><td>From:</td></tr>
    <tr><td>Fax:</td><td>Pages:</td></tr>
    <tr><td>Phone:</td><td>Date:</td></tr>
  </table>
  <div class="swirl-art" role="img" aria-label="Faint gold ribbon swirl watermark"></div>
  <svg class="band" viewBox="0 0 190 30" width="190" height="30" preserveAspectRatio="none">
    <path d="M0 14 Q95 0 190 10 L190 30 L0 30Z" fill="var(--ink)"/>
    <path d="M0 12 Q95 -2 190 8" stroke="var(--gold)" stroke-width="1.5" fill="none"/>
  </svg>
  <div class="footer-text">415-932-7104 ext 582 · www.quillmarkdeeds.example</div>
</section>

<section class="piece sheet letterhead">
  <div class="brand"><span class="brand-mark"></span><span class="brand-name">Quillmark Deeds</span></div>
  <div class="swirl-art" role="img" aria-label="Faint gold ribbon swirl watermark"></div>
  <svg class="band" viewBox="0 0 190 30" width="190" height="30" preserveAspectRatio="none">
    <path d="M0 14 Q95 0 190 10 L190 30 L0 30Z" fill="var(--ink)"/>
    <path d="M0 12 Q95 -2 190 8" stroke="var(--gold)" stroke-width="1.5" fill="none"/>
  </svg>
  <div class="footer-text">27400 W. Pelham Rd. Pine Hollow, IL · www.quillmarkdeeds.example</div>
</section>

<section class="piece envelope-c">
  <div class="brand"><span class="brand-mark"></span><span class="brand-name">Quillmark Deeds</span></div>
  <div class="swirl-art" role="img" aria-label="Faint gold ribbon swirl watermark"></div>
  <svg class="band" viewBox="0 0 216 28" width="216" height="28" preserveAspectRatio="none">
    <path d="M0 12 Q108 0 216 8 L216 28 L0 28Z" fill="var(--ink)"/>
    <path d="M0 10 Q108 -2 216 6" stroke="var(--gold)" stroke-width="1.5" fill="none"/>
  </svg>
</section>

<section class="piece notepad">
  <div class="brand"><span class="brand-mark"></span><span class="brand-name">Quillmark Deeds</span></div>
  <div class="swirl-art" role="img" aria-label="Faint gold ribbon swirl watermark"></div>
  <svg class="band" viewBox="0 0 96 22" width="96" height="22" preserveAspectRatio="none">
    <path d="M0 10 Q48 0 96 6 L96 22 L0 22Z" fill="var(--ink)"/>
    <path d="M0 8 Q48 -2 96 4" stroke="var(--gold)" stroke-width="1.2" fill="none"/>
  </svg>
</section>

<section class="piece dl-envelope dl-front">
  <div class="brand"><span class="brand-mark"></span><span class="brand-name">Quillmark Deeds</span></div>
</section>
<section class="piece dl-envelope dl-back">
  <div class="flap"></div>
  <div class="seal"></div>
</section>

<section class="piece card" style="left:439px">
  <div class="brand"><span class="brand-mark"></span><span class="brand-name">Quillmark Deeds</span></div>
  <div class="card-name">Wes Harlan</div>
  <div class="card-info">415-932-7104 ext 582<br>wessy@quillmarkdeeds.example<br>27400 W. Pelham Rd. Pine Hollow, IL</div>
</section>
<section class="piece card" style="left:533px">
  <div class="brand"><span class="brand-mark"></span><span class="brand-name">Quillmark Deeds</span></div>
  <div class="card-name">Wes Harlan</div>
  <div class="card-info">www.quillmarkdeeds.example<br>Title &amp; Escrow Services</div>
</section>
<section class="piece card card-dark" style="left:636px">
  <div class="brand"><span class="brand-mark"></span><span class="brand-name">Quillmark Deeds</span></div>
</section>
<section class="piece card card-grey" style="left:732px"></section>
<section class="piece card card-gold" style="left:828px;width:0;height:0;box-shadow:none"></section>

</body>
</html>
```